Advertising company unique advertising platform

we need a logo design for a new company based in Australia Melbourne. We develop innovated advertising platform where consumer can use this platform to get regular discount, as business owner they can use this platform for free advertisement. Payment for this advertisement platform only payable every two weeks, when I generate revenue for their business

Industry/Entity Type

Advertising

Contact Information for Business Card

Dale Pruitt | Co-Founder |Managing Director
Suite 718 263 Harrowgate Row Melbourne Vic 3000

ABN 41 902 615 273
Tel: +61 0491 528 307 | Email: dale.pruitt@corvelaxtro.com

Font styles to use
Decorative
Script

Requirements
Must have
• Try few different design and some round corner business card
Should not have
• One round corner business card...try 4 different colour background not only black, make sure two side is designed. Be creative so imagine you are giving this to a client make sure has wow factor, if you can also try one design with engrave like all the logo, words look 3d feel
• The word Advertising Platform use attached file font

```html
<!DOCTYPE html>
<html lang="en">
<head>
<meta charset="UTF-8">
<title>Trelvane Hub — Business Card</title>
<link href="https://fonts.googleapis.com/css2?family=Cormorant+Garamond:wght@500&family=Work+Sans:wght@400;500&display=swap" rel="stylesheet">
<style>
  :root {
    --page: #e9e6e1;
    --card-dark: #2b2b2c;
    --card-dark-edge: #3a3a3b;
    --card-light: #ffffff;
    --orange: #f07a22;
    --orange-soft: #f6a04d;
    --ink: #2a2a2a;
    --muted: #555555;
  }
  * { margin: 0; padding: 0; box-sizing: border-box; }
  html, body { width: 1200px; height: 900px; overflow: hidden; }
  body { background: var(--page); position: relative; font-family: "Work Sans", Arial, sans-serif; }

  .card {
    position: absolute;
    width: 560px;
    height: 320px;
    border-radius: 22px;
    overflow: hidden;
    box-shadow: 0 10px 28px rgba(0,0,0,0.18);
  }

  .card-front {
    left: 120px; top: 110px;
    background: linear-gradient(135deg, var(--card-dark-edge), var(--card-dark) 60%);
    display: flex; align-items: center; justify-content: center;
  }
  .brand {
    display: flex; align-items: center; gap: 14px;
    font-family: "Cormorant Garamond", Georgia, serif;
    font-weight: 500;
    color: var(--orange);
    letter-spacing: 0.04em;
  }
  .brand-dot { border-radius: 50%; background: var(--orange); flex: none; }
  .card-front .brand { font-size: 46px; }
  .card-front .brand-dot { width: 44px; height: 44px; }

  .card-back {
    left: 520px; top: 470px;
    background: var(--card-light);
  }
  .card-back .brand { position: absolute; left: 40px; top: 74px; font-size: 36px; gap: 10px; }
  .card-back .brand-dot { width: 30px; height: 30px; }

  .mark-area {
    position: absolute; right: 46px; top: 40px;
    width: 190px; height: 190px; border-radius: 50%;
    background: radial-gradient(circle at 40% 40%, var(--orange-soft), var(--orange));
  }

  .accent-bar {
    position: absolute; left: 0; bottom: 0;
    width: 12px; height: 150px;
    background: var(--orange);
  }

  .contact { position: absolute; left: 40px; top: 140px; }
  .person-name {
    font-family: "Cormorant Garamond", Georgia, serif;
    font-weight: 500; font-size: 28px;
    color: var(--orange); letter-spacing: 0.05em; line-height: 1;
  }
  .person-role {
    font-family: "Cormorant Garamond", Georgia, serif;
    font-size: 12px; color: var(--muted);
    letter-spacing: 0.06em; margin: 4px 0 10px;
  }
  .details { list-style: none; font-size: 13px; color: var(--ink); line-height: 1.5; }
  .details .label { color: var(--orange); margin-right: 4px; }
  .details .icon { width: 11px; height: 11px; margin-right: 8px; vertical-align: -1px; fill: var(--orange); }
</style>
</head>
<body>

  <section class="card card-front" aria-label="Card front">
    <div class="brand"><span class="brand-dot"></span>Trelvane Hub</div>
  </section>

  <section class="card card-back" aria-label="Card back">
    <div class="brand"><span class="brand-dot"></span>Trelvane Hub</div>

    <div class="mark-area" role="img" aria-label="Brand symbol area in warm orange tones"></div>

    <div class="contact">
      <h1 class="person-name">DALE PRUITT</h1>
      <p class="person-role">CO-FOUNDER | MANAGING DIRECTOR</p>
      <ul class="details">
        <li>Suite 718 263 Harrowgate Row</li>
        <li>Melbourne Vic 3000</li>
        <li><span class="label">ABN:</span>41 902 615 273</li>
        <li>
          <svg class="icon" viewBox="0 0 24 24" aria-hidden="true"><path d="M6.6 10.8a15.1 15.1 0 0 0 6.6 6.6l2.2-2.2a1 1 0 0 1 1-.25 11.4 11.4 0 0 0 3.6.57 1 1 0 0 1 1 1V20a1 1 0 0 1-1 1A17 17 0 0 1 3 4a1 1 0 0 1 1-1h3.5a1 1 0 0 1 1 1c0 1.25.2 2.45.57 3.57a1 1 0 0 1-.25 1z"/></svg>+61 0491 528 307
        </li>
        <li>
          <svg class="icon" viewBox="0 0 24 24" aria-hidden="true"><path d="M2 5h20v14H2z M4 7v.5l8 5 8-5V7z" fill-rule="evenodd"/></svg>dale.pruitt@corvelaxtro.com
        </li>
      </ul>
    </div>

    <div class="accent-bar"></div>
  </section>

</body>
</html>
```